T.K.R.A.C. Soccer Tryouts 2015-2016

I am looking for a soccer tryout flyer that stands out and catches peoples attention. An emphasis can be put on the cost, since we are by far the lowest cost program in the area. Below are the details for the flyer. I have also attached the club logo and pictures that can be used if needed.

T.K.R.A.C. SOCCER TRYOUTS
2015-2016

Club Fee: $699.00 per player

Tryout Schedule

Boys ages U9 through U14
Weds. May 27th and Friday May 29th
6:00 pm - 8:00 pm

Girls ages U9 through U14
Tuesday May 26th and Thursday May 28th
6:00 pm - 8:00 pm

All tryouts will be held at PLOV Fields
(Next to Gritmark Hardware factory at the corner of Rt. 342 and Hollow Brook Road)

We are encouraging all players to pre-register

Same Day Registrations will begin at 5:30

All players should bring a properly inflated ball, shin guards and water.

In the event of inclement weather, the tryouts will be moved to the JET indoor facility located at 4827 Dunmore Lane in Crystal Lake. The scheduled time slots will remain the same.

Website: www.tkracsoccer-example.com

Target Market(s)

Youth Soccer

Requirements
Must have
• Logo

```html
<!DOCTYPE html>
<html lang="en">
<head>
<meta charset="utf-8">
<title>T.K.R.A.C. Soccer Tryouts 2015-2016</title>
<link rel="stylesheet" href="https://fonts.googleapis.com/css2?family=Black+Ops+One&family=Oswald:wght@400;600;700&family=Special+Elite&display=swap">
<style>
  :root {
    --green: #1f7a3c;
    --green-dark: #0f4a25;
    --purple: #6a2c8e;
    --white: #ffffff;
    --grey: #d6d6d6;
    --grey-text: #4a4a4a;
    --ink: #2b2b2b;
    --page: #efefef;
  }
  * { margin: 0; padding: 0; box-sizing: border-box; }
  html, body { width: 900px; height: 1200px; overflow: hidden; background: var(--page); }
  .flyer { position: relative; width: 900px; height: 1200px; background: var(--white); overflow: hidden; font-family: "Oswald", sans-serif; }

  .brand { position: absolute; left: 40px; top: 36px; display: flex; align-items: center; gap: 14px; }
  .brand-dot { width: 54px; height: 54px; border-radius: 50%; background: var(--green); }
  .brand-name { font-weight: 700; font-size: 40px; color: var(--green); letter-spacing: 1px; }

  .headline { position: absolute; right: 36px; top: 28px; text-align: right; }
  .headline-title { font-weight: 700; font-size: 44px; color: var(--green); letter-spacing: 1px; line-height: 1.1; }
  .headline-year { font-family: "Black Ops One", sans-serif; font-size: 118px; color: var(--purple); line-height: 1; margin-top: 4px; }

  .team-photo { position: absolute; left: 0; top: 210px; width: 580px; height: 470px;
    background: linear-gradient(160deg, #9cc7e8 0%, #6fa4cf 45%, #4f8a3e 80%, #3d6f2f 100%);
    clip-path: polygon(0 0, 100% 0, 100% 78%, 0 100%); }

  .fee { position: absolute; right: 40px; top: 260px; text-align: right; }
  .fee-label { font-weight: 700; font-size: 64px; color: var(--ink); line-height: 1; }
  .fee-amount { font-weight: 700; font-size: 92px; color: var(--purple); line-height: 1.05; }
  .fee-unit { font-weight: 700; font-size: 60px; color: var(--ink); line-height: 1; }

  .stripes { position: absolute; left: 0; top: 520px; width: 900px; height: 240px; }

  .sessions { position: absolute; left: 30px; top: 720px; width: 840px; height: 170px; display: flex; gap: 20px; }
  .session { flex: 1; padding: 22px 12px; font-family: "Special Elite", monospace; text-transform: uppercase; text-align: center; }
  .session-boys { background: var(--white); color: var(--purple); border: 3px solid var(--purple); }
  .session-girls { background: var(--grey); color: var(--grey-text); }
  .session-group { font-size: 23px; line-height: 1.25; white-space: nowrap; }
  .session-dates { font-size: 15px; line-height: 1.3; margin-top: 8px; white-space: nowrap; }
  .session-time { font-family: "Oswald", sans-serif; font-weight: 700; font-size: 36px; margin-top: 14px; }
  .session-girls .session-time { color: var(--purple); }

  .same-day { position: absolute; left: 0; top: 910px; width: 900px; height: 82px; background: var(--green-dark);
    color: var(--white); font-weight: 700; font-size: 44px; text-align: center; line-height: 82px; letter-spacing: 1px; }

  .preregister { position: absolute; left: 0; top: 1000px; width: 900px; height: 80px; display: flex; align-items: center; justify-content: center; gap: 18px; }
  .preregister-lead { font-weight: 600; font-size: 34px; color: var(--green); }
  .preregister-cta { background: var(--purple); color: var(--white); font-weight: 700; font-size: 44px; padding: 2px 22px; }

  .footer { position: absolute; left: 0; top: 1088px; width: 900px; height: 112px; background: var(--green-dark); overflow: hidden; }
  .footer-stripes { position: absolute; inset: 0; }
  .footer-web { position: absolute; left: 30px; top: 60px; font-weight: 700; font-size: 26px; line-height: 36px; color: var(--white); letter-spacing: 1px; white-space: nowrap; }
  .footer-address { position: absolute; right: 0; top: 14px; height: 50px; padding: 0 30px 0 40px; background: var(--purple);
    color: var(--white); font-weight: 700; font-size: 24px; line-height: 50px; white-space: nowrap;
    clip-path: polygon(20px 0, 100% 0, 100% 100%, 0 100%); }
</style>
</head>
<body>
<main class="flyer">
  <div class="team-photo" role="img" aria-label="Photo of the girls youth soccer team in light blue jerseys with their coach on a grass field"></div>

  <header>
    <div class="brand"><span class="brand-dot"></span><span class="brand-name">T.K.R.A.C.</span></div>
    <div class="headline">
      <h1 class="headline-title">T.K.R.A.C. SOCCER TRYOUTS</h1>
      <p class="headline-year">2015-2016</p>
    </div>
  </header>

  <section class="fee">
    <p class="fee-label">CLUB FEE</p>
    <p class="fee-amount">$699.00</p>
    <p class="fee-unit">PER PLAYER</p>
  </section>

  <svg class="stripes" viewBox="0 0 900 240" aria-hidden="true">
    <polygon points="0,150 900,0 900,40 0,190" fill="var(--white)"/>
    <polygon points="0,170 900,20 900,70 0,220" fill="var(--purple)"/>
    <polygon points="0,215 900,65 900,95 0,240" fill="var(--green)"/>
    <polygon points="0,240 900,95 900,240" fill="var(--white)"/>
  </svg>

  <section class="sessions">
    <div class="session session-boys">
      <p class="session-group">Boys ages U9 through U14</p>
      <p class="session-dates">Weds. May 27th and Friday May 29th</p>
      <p class="session-time">6:00 PM - 8:00 PM</p>
    </div>
    <div class="session session-girls">
      <p class="session-group">Girls ages U9 through U14</p>
      <p class="session-dates">Tuesday May 26th and Thursday May 28th</p>
      <p class="session-time">6:00 PM - 8:00 PM</p>
    </div>
  </section>

  <p class="same-day">SAME DAY REGISTRATIONS WILL BEGIN AT 5:30</p>

  <div class="preregister">
    <span class="preregister-lead">WE ARE ENCOURAGING ALL PLAYERS TO</span>
    <span class="preregister-cta">PRE-REGISTER</span>
  </div>

  <footer class="footer">
    <svg class="footer-stripes" viewBox="0 0 900 112" aria-hidden="true">
      <polygon points="0,20 300,0 340,0 0,50" fill="var(--green)"/>
      <polygon points="0,70 520,0 560,0 0,100" fill="var(--green)"/>
    </svg>
    <p class="footer-address">RT. 342 AND HOLLOW BROOK ROAD</p>
    <p class="footer-web">WWW.TKRACSOCCER-EXAMPLE.COM</p>
  </footer>
</main>
</body>
</html>
```